依頼詳細
今年の仮チラシをファイル添付しておきますので、講師の肩書、名前等の確認をお願いいたします。

昨年の講演会のチラシもファイル添付しておきますので、参考にお願いいたします。

こどもさんの笑顔の写真や、家族で幸せそうにしている写真がありそうでしたら、多めに使用していただけますか。
記載項目
記載項目は基本2018年のチラシと同じですので、ファイル添付分で確認をおねがいします。(日付だけが、9月21日(土)となります。)
サイズ
A4
ページ数
片面
希望イメージ
シンプル 複雑
単色 カラフル
暗い 明るい
日常 高級
遊び心 厳粛
未来的 伝統的
女性的 男性的
希望する色
水色系、緑系、黄・オレンジ系
納品ファイル
• 高解像度JPG (.jpg)
補足説明
今年の講演会チラシにも講師二人の写真を入れる予定です。撮影できしだいファイルをおくるかたちとなります。よろしくお願いいたします。
■ 選んだ理由

イメージと合ったから。

■ 提案者全員のお礼・コメント

みなさん、ご協力ありがとうございました。

```html
<!DOCTYPE html>
<html lang="ja">
<head>
<meta charset="utf-8">
<title>こどもの栄養 こどもの姿勢 講演会</title>
<link href="https://fonts.googleapis.com/css2?family=M+PLUS+Rounded+1c:wght@500;700;800&family=Noto+Sans+JP:wght@400;500;700&display=swap" rel="stylesheet">
<style>
:root{
  --orange:#f39a1e;
  --yellow:#f7c325;
  --green:#7cc242;
  --sky:#8fd1ee;
  --sky-deep:#3aa7d9;
  --red:#e4344a;
  --ink:#3b3b3b;
  --muted:#6b6b6b;
  --paper:#ffffff;
  --cream:#fffbea;
}
*{margin:0;padding:0;box-sizing:border-box}
html,body{width:849px;height:1200px;overflow:hidden;background:var(--paper)}
body{font-family:"Noto Sans JP",sans-serif;color:var(--ink);position:relative}
.hero{position:absolute;left:0;top:0;width:849px;height:480px;overflow:hidden}
.photo{position:absolute}
.photo-a{left:0;top:0;width:430px;height:300px;background:linear-gradient(135deg,#6fae4a,#c8e07a 60%,#f2c97a)}
.photo-b{left:430px;top:0;width:419px;height:300px;background:linear-gradient(160deg,#7fc8f0,#cfeefc 55%,#9bd4a0)}
.photo-c{left:0;top:300px;width:430px;height:180px;background:linear-gradient(120deg,#e8b48a,#7fb85a 70%)}
.photo-d{left:430px;top:300px;width:419px;height:180px;background:linear-gradient(200deg,#6fc3ea,#f2d7b6 60%,#eaa0a8)}
.title-circle{position:absolute;width:258px;height:258px;border-radius:50%;display:flex;flex-direction:column;align-items:center;justify-content:center;color:#fff;font-family:"M PLUS Rounded 1c",sans-serif;font-weight:800;border:5px solid rgba(255,255,255,.85)}
.title-circle .sub{font-size:34px;letter-spacing:2px;line-height:1.1}
.title-circle .main{font-size:76px;line-height:1.15;letter-spacing:4px}
.circle-nutrition{left:196px;top:150px;background:var(--orange);opacity:.95}
.circle-posture{left:396px;top:150px;background:var(--green);opacity:.93}
.ribbon{position:absolute;left:200px;top:440px;width:450px;height:46px}
.ribbon-text{position:absolute;left:200px;top:440px;width:450px;height:46px;display:flex;align-items:center;justify-content:center;color:#fff;font-family:"M PLUS Rounded 1c",sans-serif;font-weight:700;font-size:22px;letter-spacing:2px}
.intro{position:absolute;left:40px;top:580px;width:770px;text-align:center;color:var(--red);font-size:17px;line-height:1.85;font-weight:500}
.speakers-head{position:absolute;left:0;top:680px;width:849px;text-align:center;font-family:"M PLUS Rounded 1c",sans-serif;font-weight:700;font-size:24px;letter-spacing:6px}
.speakers-head::before,.speakers-head::after{content:"";display:inline-block;width:60px;height:2px;background:var(--sky-deep);vertical-align:middle;margin:0 16px}
.speaker{position:absolute;top:720px;width:380px;height:215px;border:2px solid var(--sky);border-radius:10px;background:var(--cream);padding:14px}
.speaker-left{left:36px}
.speaker-right{left:432px}
.speaker-role{position:absolute;left:140px;top:14px;font-size:13px;color:var(--muted)}
.speaker-name{position:absolute;left:140px;top:32px;font-size:20px;font-weight:700;font-family:"M PLUS Rounded 1c",sans-serif}
.speaker-name small{font-size:14px}
.speaker-photo{position:absolute;left:14px;top:14px;width:112px;height:140px;border-radius:6px;background:linear-gradient(160deg,#d7ecf7,#a9d6ea)}
.speaker-bio{position:absolute;left:140px;top:70px;right:14px;font-size:12.5px;line-height:1.7;color:var(--ink)}
.event{position:absolute;left:40px;top:965px;width:500px}
.era{display:inline-block;background:var(--orange);color:#fff;font-size:15px;font-weight:700;padding:3px 10px;border-radius:4px}
.date-row{display:flex;align-items:flex-end;gap:12px;margin-top:4px}
.date{font-family:"M PLUS Rounded 1c",sans-serif;font-weight:800;color:var(--orange);font-size:70px;line-height:1}
.date .unit{font-size:38px}
.dow{display:inline-flex;width:42px;height:42px;border-radius:50%;background:var(--sky-deep);color:#fff;font-size:22px;font-weight:700;align-items:center;justify-content:center;margin-bottom:8px}
.times{font-size:16px;line-height:1.45;margin-bottom:6px;font-weight:500}
.details{margin-top:8px;font-size:17px;line-height:1.6}
.details .label{color:var(--orange);font-weight:700}
.details .fee{font-size:22px;font-weight:700}
.details .address{font-size:13px;color:var(--muted)}
.map{position:absolute;left:550px;top:975px;width:265px;height:165px;border:2px solid var(--sky);background:#fff;display:flex;align-items:center;justify-content:center;font-size:30px;color:var(--ink)}
.organizer{position:absolute;left:40px;top:1160px;font-size:14px;font-weight:500}
.organizer small{font-size:11px;color:var(--muted);margin-left:10px}
</style>
</head>
<body>
<section class="hero">
  <div class="photo photo-a" role="img" aria-label="野菜を食べて笑う子どもの写真"></div>
  <div class="photo photo-b" role="img" aria-label="青空の下で手を広げる子どもの写真"></div>
  <div class="photo photo-c" role="img" aria-label="芝生で遊ぶ家族の写真"></div>
  <div class="photo photo-d" role="img" aria-label="寝転んで笑う子どもたちの写真"></div>
  <div class="title-circle circle-nutrition"><span class="sub">こどもの</span><span class="main">栄養</span></div>
  <div class="title-circle circle-posture"><span class="sub">こどもの</span><span class="main">姿勢</span></div>
</section>
<svg class="ribbon" viewBox="0 0 450 46" aria-hidden="true">
  <polygon points="0,8 30,8 30,40 0,40 14,24" fill="#2f8fc2"/>
  <polygon points="450,8 420,8 420,40 450,40 436,24" fill="#2f8fc2"/>
  <rect x="22" y="2" width="406" height="38" rx="4" fill="#3aa7d9"/>
</svg>
<div class="ribbon-text">こども達の輝かしい未来のために</div>

<p class="intro">平成17年に食育基本法が制定されて以来、長年学校教育で児童の栄養指導を行ってきた<br>こどもの栄養専門家と大学で姿勢の専門家を育ててきた博士（健康科学）によるコラボレーション講演会</p>

<h2 class="speakers-head">講師紹介</h2>

<article class="speaker speaker-left">
  <div class="speaker-photo" role="img" aria-label="講師の顔写真"></div>
  <p class="speaker-role">管理栄養士</p>
  <p class="speaker-name">青木奈央 <small>氏</small></p>
  <p class="speaker-bio">学校給食におけるアレルギー対策、自分の体を守るためにはどのようにしたらよいかの食育など、こどもにバランスの取れた食事を提供するために工夫してきました。</p>
</article>
<article class="speaker speaker-right">
  <div class="speaker-photo" role="img" aria-label="講師の顔写真"></div>
  <p class="speaker-role">健康科学博士</p>
  <p class="speaker-name">川端直樹 <small>氏</small></p>
  <p class="speaker-bio">こどもの姿勢はいつ、どのように形成されるのか。赤ちゃんが歩き始めるまでに大切な関わり方とは。ハッピーマッサージで親子の絆を深め、こどもの姿勢の基本を学びます。</p>
</article>

<section class="event">
  <span class="era">令和元年</span>
  <div class="date-row">
    <div class="date">9<span class="unit">月</span>21<span class="unit">日</span></div>
    <span class="dow">土</span>
    <div class="times">開場 13：00〜<br>開演 13：30</div>
  </div>
  <div class="details">
    <p><span class="label">参加費</span>　<span class="fee">4,000円</span></p>
    <p><span class="label">場所</span>　ひかりプラザ洛南 2階ホール</p>
    <p class="address">〒600-0000 京都市南区ひかり町1-23</p>
  </div>
</section>
<div class="map" role="img" aria-label="会場までの地図">map</div>
<p class="organizer">主催：洛南こども姿勢研究会<small>お問い合わせは会事務局まで</small></p>
</body>
</html>
```